Velora Reggaeton Night

I'd like to create a flyer / poster for a reaggaeton Xmas party in London. The party will be titled "Velora" and will be VIP for friends of friends only. The concept has to remain classy and stylish as I don't want it to be related to anything tropical at first glance. People attending the party will be a bit up-scale so the style is key. I am thinking of a black background and golden or silver letters, which give a bit of a "bling" look. Since the party will take place in Central London, I was thinking perhaps including something that relates to the city (St. Ambrin's Cathedral, the Quillon, etc.). I have seen a few ideas and I am happy to send those over to illustrate a bit better what I am thinking of. Color wise, the theme could be very black and grey (for the London buildings) and only keep a few bright red colors if including London double decker buses or phone booths. Need to include something that gives the poster / flyer a Latin vibe as well.

Target Market(s)

25-35 year olds. Young professionals living in London. Latin American and European origins. People that enjoy dancing and like reggaeton music in particular.

Industry/Entity Type

Latin American Café

Requirements
Must have
• Must have the name of the party, VELORA, as a big part of the flyer. Also the words "reggaeton party" or "reggaeton night". Something catchy. The date will be December 16 2017. Time will be 7pm to 3am. Location is Central London (Bank). I don't want to specify the location as I want it to be "secret" and only people with the ticket will be given the address.
Nice to have
• Nice to have something that resembles London but also the Latin, bling vibe of reggaeton music. Velora means "flirt" in Spanish so I want the design to be flirty but elegant and very stylish. VELORA could be written in Gold or Silver to make it stand-out. Could be made up of yellow light bulbs as well. And could include a rose to make it more flirty. See examples attached.
Should not have
• Typical tropical or Cuban type designs. I don't want anything too colorful as I want to keep it classy and stylish. Try to avoid people dancing in the flyer. Don't want a photo of sexy women in the flyer. Need to keep it classy.

```html
<!DOCTYPE html>
<html lang="en">
<head>
<meta charset="utf-8">
<title>Velora London – Reggaeton Night</title>
<link rel="stylesheet" href="https://fonts.googleapis.com/css2?family=Montserrat:wght@600;700&family=Great+Vibes&family=Oswald:wght@400;500&display=swap">
<style>
  :root {
    --page-bg: #f4f4f4;
    --frame-grey: #8d8d8d;
    --night: #050403;
    --gold-light: #f6dfa4;
    --gold: #d9a84e;
    --gold-deep: #9a6a22;
    --lime: #8fc43a;
    --emerald: #1f5a36;
    --ink-white: #ffffff;
    --cream: #f1e6d2;
  }
  html, body {
    margin: 0;
    width: 1200px;
    height: 1200px;
    overflow: hidden;
    background: var(--page-bg);
  }
  .poster {
    position: absolute;
    left: 200px;
    top: 11px;
    width: 800px;
    height: 1177px;
    box-shadow: 0 0 14px rgba(0,0,0,0.25);
  }
  .poster svg { display: block; width: 100%; height: 100%; }
  .brand-name { font-family: "Montserrat", sans-serif; font-weight: 700; fill: var(--ink-white); }
  .city-name { font-family: "Montserrat", sans-serif; font-weight: 700; fill: var(--ink-white); letter-spacing: 4px; }
  .script-title { font-family: "Great Vibes", cursive; fill: url(#goldText); }
  .event-time { font-family: "Oswald", sans-serif; font-weight: 500; fill: var(--cream); }
  .event-date { font-family: "Montserrat", sans-serif; font-weight: 700; fill: var(--ink-white); }
  .footer-line { font-family: "Oswald", sans-serif; font-weight: 400; fill: var(--cream); letter-spacing: 8px; }
</style>
</head>
<body>
<div class="poster">
<svg viewBox="0 0 1006 1480" xmlns="http://www.w3.org/2000/svg">
  <defs>
    <radialGradient id="skyGlow" cx="0.6" cy="0.2" r="0.7">
      <stop offset="0" stop-color="#e8e23a"/>
      <stop offset="0.3" stop-color="#a78a12"/>
      <stop offset="0.6" stop-color="#4a2206"/>
      <stop offset="1" stop-color="#050403"/>
    </radialGradient>
    <linearGradient id="goldText" x1="0" y1="0" x2="0" y2="1">
      <stop offset="0" stop-color="#fbe7b0"/>
      <stop offset="0.5" stop-color="#d9a84e"/>
      <stop offset="1" stop-color="#8a5a18"/>
    </linearGradient>
    <linearGradient id="goldRule" x1="0" y1="0" x2="1" y2="0">
      <stop offset="0" stop-color="#d9a84e" stop-opacity="0"/>
      <stop offset="0.5" stop-color="#f6c860"/>
      <stop offset="1" stop-color="#d9a84e" stop-opacity="0"/>
    </linearGradient>
    <linearGradient id="skylineTone" x1="0" y1="0" x2="0" y2="1">
      <stop offset="0" stop-color="#d9a84e" stop-opacity="0.15"/>
      <stop offset="1" stop-color="#d9a84e" stop-opacity="0.45"/>
    </linearGradient>
    <linearGradient id="emeraldSpark" x1="0" y1="0" x2="1" y2="1">
      <stop offset="0" stop-color="#123a22"/>
      <stop offset="0.5" stop-color="#2c6b3c"/>
      <stop offset="1" stop-color="#0f2e1b"/>
    </linearGradient>
    <linearGradient id="lowerPrism" x1="0" y1="0" x2="1" y2="0">
      <stop offset="0" stop-color="#2a2a26"/>
      <stop offset="0.5" stop-color="#1c3324"/>
      <stop offset="1" stop-color="#2a2a26"/>
    </linearGradient>
  </defs>

  <!-- frame -->
  <rect class="poster-frame" width="1006" height="1480" fill="var(--frame-grey)"/>
  <rect class="poster-ground" x="8" y="8" width="990" height="1464" fill="var(--night)"/>

  <!-- fireworks sky -->
  <rect class="fireworks-sky" x="8" y="8" width="990" height="1100" fill="url(#skyGlow)" role="img" aria-label="Golden fireworks bursting over the night sky"/>
  <rect x="8" y="900" width="990" height="220" fill="var(--night)" opacity="0.7"/>

  <!-- skylines -->
  <rect class="skyline-left" x="20" y="570" width="175" height="315" fill="url(#skylineTone)" role="img" aria-label="Gold line drawing of a London skyline with an observation wheel"/>
  <rect class="skyline-right" x="735" y="570" width="250" height="325" fill="url(#skylineTone)" role="img" aria-label="Gold line drawing of a London clock tower and a curved glass tower"/>

  <!-- prism emblem -->
  <g class="prism">
    <polygon points="503,140 228,760 778,760" fill="url(#emeraldSpark)" role="img" aria-label="Triangle filled with sparkling green lights"/>
    <polygon points="503,275 385,455 621,455" fill="var(--lime)"/>
    <polygon points="362,455 644,455 666,505 340,505" fill="var(--night)"/>
    <polygon points="303,545 708,545 503,755" fill="#1d5a3a" role="img" aria-label="Inverted triangle filled with green glitter"/>
    <polygon points="228,760 303,545 420,760" fill="var(--night)" opacity="0.85"/>
    <polygon points="778,760 708,545 586,760" fill="var(--night)" opacity="0.85"/>
    <polygon points="503,665 430,760 576,760" fill="#c9dc4a"/>
  </g>

  <!-- lower prism -->
  <polygon class="lower-prism" points="138,1060 868,1060 503,770" fill="url(#lowerPrism)" role="img" aria-label="Dark triangle with faint green firework texture"/>

  <!-- title block -->
  <rect class="title-plate" x="193" y="760" width="615" height="133" fill="var(--night)"/>
  <text class="brand-name" x="498" y="862" font-size="104" text-anchor="middle" letter-spacing="2">VELORA</text>
  <text class="city-name" x="223" y="930" font-size="50">LONDON</text>
  <text class="script-title" x="250" y="1045" font-size="120" transform="rotate(-20 480 1000)">Reggaeton</text>
  <text class="script-title" x="470" y="1110" font-size="120" transform="rotate(-20 600 1070)">Night</text>

  <!-- details -->
  <rect x="20" y="1121" width="966" height="3" fill="url(#goldRule)"/>
  <text class="event-time" x="500" y="1195" font-size="58" text-anchor="middle">7PM - 3AM</text>
  <rect x="20" y="1212" width="966" height="3" fill="url(#goldRule)"/>
  <text class="event-date" x="500" y="1280" font-size="52" text-anchor="middle" letter-spacing="2">SATURDAY</text>
  <text class="event-date" x="500" y="1333" font-size="55" text-anchor="middle" letter-spacing="1">DECEMBER 16<tspan font-size="30" dy="-22">TH</tspan><tspan dy="22"> 2017</tspan></text>
  <rect x="20" y="1334" width="966" height="3" fill="url(#goldRule)"/>
  <text class="footer-line" x="500" y="1393" font-size="26" text-anchor="middle">CENTRAL LONDON</text>
  <text class="footer-line" x="500" y="1435" font-size="29" text-anchor="middle">FOLLOW US @VELORALONDON</text>
</svg>
</div>
</body>
</html>
```